Web design for a Senior Home Care company

I want a web design for a home care company called Willowmere Home Care. What WHC does is send caregivers into people's homes to assist with daily living needs such as companionship, food preparation, cleaning, bathing, using the bathroom, etc. Most of the clients are seniors. The people deciding to use WHC are usually the 50 year old children of these senior citizens. Most visitors to the site will be women searching for this service for their parents.

The call to action is to inspire the website visitors to call us to set up an appointment to meet them in their home. The site design should inspire confidence in Willowmere Home Care to care for people's needs. We want to show the same attributes that a parent should have. Safety, Security and Loving Care.

Again, the goal of the site is to inspire and make it EASY for visitors to contact us either by phone call or through the website. The first choice is that they call us.

To help you with your ideas, In the attachments I've included different versions of our logo, a site map, examples of photos we might use and very rough draft of the website copy.

Target Market(s)

The customers will mostly be seniors. But, the people who will decide to use the company will the the 50 year old children of those seniors. Also, it is mostly women who are looking for help for their parents.

Industry/Entity Type

It Company

Number of Pages Required

5+ page

Requirements
Nice to have
• I want site visitors to easily be able to contact us with a phone call or through the website. The home page should inspire people to call us.

```html
<!DOCTYPE html>
<html lang="en">
<head>
<meta charset="utf-8">
<title>Willowmere Home Care</title>
<link href="https://fonts.googleapis.com/css2?family=Cinzel:wght@400;600&family=Open+Sans:ital,wght@0,400;0,600;0,700;1,400&display=swap" rel="stylesheet">
<style>
:root{
  --blue:#1a7cc9;
  --blue-dark:#0f5fa3;
  --blue-light:#3a9be0;
  --ink:#222;
  --text:#444;
  --muted:#777;
  --line:#cfcfcf;
  --grey-bg:#eeeeee;
  --footer:#2b2b2b;
  --white:#fff;
}
*{box-sizing:border-box;margin:0;padding:0}
html,body{width:1200px;height:3077px;overflow:hidden;background:var(--white)}
body{font-family:"Open Sans",Arial,sans-serif;color:var(--text);position:relative}
.abs{position:absolute}
h2.section-title{font-family:"Cinzel",Georgia,serif;font-weight:400;font-size:33px;color:var(--ink);letter-spacing:1px}
h2.section-title span{color:var(--blue)}
.divider{position:absolute;height:20px;display:flex;align-items:center;gap:8px}
.divider i{display:block;height:1px;background:var(--line);flex:1}
.btn{position:absolute;background:var(--blue);color:#fff;font-weight:600;font-size:14px;display:flex;align-items:center;justify-content:center;text-transform:uppercase;border-radius:2px}

/* header */
.topline{left:0;top:0;width:1200px;height:5px;background:#333}
.phone-tab{left:885px;top:0;width:205px;height:30px;background:#2d2d2d;color:#fff;font-size:17px;display:flex;align-items:center;justify-content:center;gap:10px;border-radius:0 0 14px 14px}
.brand{left:100px;top:26px;display:flex;align-items:center;gap:14px}
.brand .mark{width:62px;height:62px;background:var(--blue);border-radius:4px}
.brand .name{font-family:"Cinzel",Georgia,serif;font-size:28px;line-height:30px;color:var(--blue);font-weight:600}
.search{left:878px;top:58px;width:222px;height:30px;border:1px solid #ccc;font-size:12px;color:#999;padding:7px 12px}
.search svg{position:absolute;right:10px;top:7px}
.nav{left:0;top:118px;width:1200px;height:38px;background:linear-gradient(#2b8ddb,#176fb8);display:flex;padding-left:100px}
.nav a{color:#fff;font-size:13.5px;text-decoration:none;height:38px;display:flex;align-items:center;padding:0 24px}
.nav a.active{background:#0e5a9c}

/* hero */
.hero{left:0;top:156px;width:1200px;height:513px;background:linear-gradient(90deg,#e9e9e9,#f4f4f4 45%,#dcdcdc)}
.hero-photo{left:560px;top:156px;width:640px;height:513px;background:linear-gradient(160deg,#d9d6d2,#b7aea8 50%,#8a8691)}
.hero-title{left:100px;top:335px;font-weight:400;font-size:33px;color:var(--ink)}
.hero-rule{left:100px;top:384px;width:385px;height:1px;background:#999}
.hero-sub{left:100px;top:396px;font-size:22px;color:#333}
.dots{left:568px;top:622px;display:flex;gap:5px}
.dots b{width:11px;height:11px;border-radius:50%;border:2px solid #fff;background:transparent}
.dots b.on{background:#fff}

/* about */
.about-sub{left:100px;top:800px;color:var(--blue);font-size:15.5px;font-weight:600}
.about-text{left:100px;top:832px;width:605px;font-size:13.5px;line-height:24px;color:#333}
.about-photo{left:722px;top:715px;width:375px;height:283px;border:5px solid #fff;box-shadow:0 0 0 1px #ddd;background:linear-gradient(135deg,#7aa66a,#c7b7a6 55%,#8c6c5a)}

/* services */
.services{left:0;top:1040px;width:1200px;height:500px;background:linear-gradient(100deg,#eef0f4,#e6e1df 40%,#ececef 70%,#dfe2e8)}
.services-intro{left:100px;top:1170px;width:1000px;text-align:center;font-size:13px;line-height:23px;color:#333}
.card{position:absolute;top:1225px;width:230px;text-align:center}
.card .pic{height:152px;border:4px solid #fff;box-shadow:0 1px 3px rgba(0,0,0,.2)}
.card h3{font-family:"Cinzel",Georgia,serif;font-weight:600;font-size:16px;color:var(--ink);margin-top:20px;letter-spacing:1px}
.card p{font-size:12.5px;line-height:20px;color:#333;height:40px;overflow:hidden;margin-top:4px}
.card .plus{width:22px;height:22px;background:var(--blue);color:#fff;margin:14px auto 0;display:flex;align-items:center;justify-content:center;font-weight:700;font-size:16px}
.arrow{position:absolute;top:1285px}

/* why */
.why{left:0;top:1540px;width:1200px;height:390px;background:#ededed}
.why-text{left:100px;top:1667px;width:660px;font-size:13px;line-height:24px;color:#333}
.checks{position:absolute;top:1730px;list-style:none;font-size:13.5px;color:#333}
.checks li{height:32px;display:flex;align-items:center;gap:10px}
.checks svg{flex:none}
.why-photo{left:787px;top:1675px;width:313px;height:210px;border:5px solid #fff;box-shadow:0 0 0 1px #ddd;background:linear-gradient(120deg,#9bc4d6,#a57d63 45%,#d0b4a0 70%,#5f6d80)}

/* news & faq */
.pager{left:523px;top:1990px;display:flex;gap:4px}
.pager b{width:14px;height:14px;border-radius:50%;border:1px solid #e77;font-size:9px;display:flex;align-items:center;justify-content:center;color:#e77}
.pager b.next{border-color:#3a3;color:#3a3}
.news-item{position:absolute;left:100px;width:450px;height:70px}
.date{position:absolute;left:0;top:0;width:64px;height:58px;border:1px solid #ccc;background:#fff;text-align:center}
.date .m{background:var(--blue);color:#fff;font-size:12px;height:22px;line-height:22px;font-weight:600}
.date .d{font-size:18px;color:#222;line-height:34px}
.news-item h4{position:absolute;left:66px;top:0;width:384px;font-size:12px;line-height:18px;font-weight:700;color:#222;white-space:nowrap;overflow:hidden}
.news-item p{position:absolute;left:66px;top:19px;width:384px;font-size:12px;line-height:17px;color:#444}
.faq{position:absolute;left:635px;width:465px;height:34px;background:#e9e9e9;font-size:13px;font-weight:600;color:#333;display:flex;align-items:center;padding-left:12px}
.faq .toggle{position:absolute;right:10px;top:9px;width:16px;height:16px;border-radius:50%;background:#444;color:#fff;font-size:13px;line-height:16px;text-align:center}
.faq.open{background:var(--blue);color:#fff}
.faq.open .toggle{background:#fff;color:var(--blue)}
.faq-body{left:635px;top:2236px;width:465px;height:64px;border:1px solid var(--blue);border-top:none;font-size:12.5px;line-height:19px;color:#333;padding:10px 18px}

/* reviews */
.reviews{left:0;top:2340px;width:1200px;height:385px;background:#eeeeee}
.avatar{position:absolute;top:2486px;width:86px;height:86px;border-radius:50%;border:4px solid #fff;box-shadow:0 0 0 1px #ccc}
.avatar.active{box-shadow:0 0 0 3px var(--blue)}
.quote{left:150px;top:2594px;width:900px;text-align:center;font-style:italic;font-size:12.5px;line-height:28px;color:#555}
.qmark{font-family:Georgia,serif;font-style:normal;font-size:48px;color:#8cc0ea;line-height:0;vertical-align:-16px;margin:0 8px}

/* footer */
.footer{left:0;top:2725px;width:1200px;height:308px;background:var(--footer)}
.footer-title{position:absolute;top:2765px;font-family:"Cinzel",Georgia,serif;font-weight:400;font-size:17px;color:#fff;letter-spacing:1px;padding-bottom:10px;border-bottom:1px solid #555}
.quick-links{position:absolute;left:100px;top:2810px;list-style:none;font-size:12.5px;color:#ddd}
.quick-links li{height:22px}
.quick-links li::before{content:"›";margin-right:7px;color:#aaa}
.contact{position:absolute;left:313px;font-size:13.5px;color:#eee;display:flex;gap:10px}
.field{position:absolute;left:613px;width:272px;background:#fff;font-size:12px;color:#666;padding:8px 10px}
.footer-brand{left:935px;top:2810px;width:170px;text-align:center}
.footer-brand .mark{width:60px;height:60px;border:2px solid #aaa;margin:0 auto 10px}
.footer-brand .name{font-family:"Cinzel",Georgia,serif;font-size:24px;line-height:28px;color:#bbb}
.copyright{left:0;top:3033px;width:1200px;height:44px;background:var(--blue);color:#fff;font-size:13px;display:flex;align-items:center;justify-content:center}
</style>
</head>
<body>

<!-- Header -->
<div class="abs topline"></div>
<div class="abs phone-tab">
  <svg width="14" height="14" viewBox="0 0 24 24"><path fill="#fff" d="M6.6 10.8a15 15 0 0 0 6.6 6.6l2.2-2.2c.3-.3.7-.4 1-.2 1.1.4 2.3.6 3.6.6.6 0 1 .4 1 1V20c0 .6-.4 1-1 1A17 17 0 0 1 3 4c0-.6.4-1 1-1h3.5c.6 0 1 .4 1 1 0 1.3.2 2.5.6 3.6.1.3 0 .7-.2 1z"/></svg>
  555.014.2290
</div>
<div class="abs brand">
  <div class="mark"></div>
  <div class="name">Willowmere<br>Home Care</div>
</div>
<div class="abs search">Search
  <svg width="14" height="14" viewBox="0 0 24 24"><circle cx="10" cy="10" r="6" fill="none" stroke="#999" stroke-width="2"/><path d="M15 15l5 5" stroke="#999" stroke-width="2"/></svg>
</div>
<nav class="abs nav">
  <a class="active">Home</a><a>About Us</a><a>Services</a><a>Free In-Home Consultation</a><a>News</a><a>Reviews</a><a>FAQ</a><a>Client Portal</a><a>Contact Us</a>
</nav>

<!-- Hero -->
<section class="abs hero"></section>
<div class="abs hero-photo" role="img" aria-label="Smiling caregiver with an arm around an elderly man holding a cane"></div>
<h1 class="abs hero-title">Willowmere Home Care</h1>
<div class="abs hero-rule"></div>
<div class="abs hero-sub">Family-Owned, Service You Can Trust</div>
<div class="btn" style="left:100px;top:432px;width:153px;height:42px;font-size:15px">Contact Now</div>
<div class="abs dots"><b class="on"></b><b></b><b></b><b></b></div>

<!-- About -->
<h2 class="abs section-title" style="left:100px;top:705px">About <span>Us</span></h2>
<div class="divider" style="left:100px;top:752px;width:580px">
  <svg width="24" height="20" viewBox="0 0 24 20"><path d="M3 10L12 2l9 8M6 8v10h12V8" fill="none" stroke="#777" stroke-width="1.5"/></svg><i></i>
</div>
<div class="abs about-sub">The Reason We Started Willowmere Home Care Is Simple</div>
<p class="abs about-text">we love people. We've experienced home care before and knew we can do it better. My husband and I know the process can be confusing, time consuming and stressful, but it shouldn't be. We decided to do our part by making everything as simple, safe and easy as possible. Often times, when you're searching and call a home care company, you'll find out later you've reached a referral service or registry, not an actual home care provider.</p>
<div class="btn" style="left:100px;top:964px;width:128px;height:34px;font-size:13px">Read More</div>
<div class="abs about-photo" role="img" aria-label="Caregiver in green sharing a laugh with a senior woman"></div>

<!-- Services -->
<section class="abs services" role="img" aria-label="Soft blurred background of caring hands"></section>
<h2 class="abs section-title" style="left:0;width:1200px;text-align:center;top:1078px">Our <span>Services</span></h2>
<div class="divider" style="left:405px;top:1126px;width:390px"><i></i><svg width="24" height="20" viewBox="0 0 24 20"><path d="M3 10L12 2l9 8M6 8v10h12V8" fill="none" stroke="#777" stroke-width="1.5"/></svg><i></i></div>
<p class="abs services-intro">Willowmere Home Care offers a wide variety of home care services, from once a week visits to 24-hour care. Since every situation is unique, we work together with you to create the perfect program.</p>
<svg class="arrow" style="left:62px" width="16" height="30" viewBox="0 0 16 30"><path d="M14 2L3 15l11 13" fill="none" stroke="#aaa" stroke-width="2"/></svg>
<svg class="arrow" style="left:1120px" width="16" height="30" viewBox="0 0 16 30"><path d="M2 2l11 13L2 28" fill="none" stroke="#aaa" stroke-width="2"/></svg>
<div class="card" style="left:98px">
  <div class="pic" role="img" aria-label="Senior and caregiver playing cards together" style="background:linear-gradient(135deg,#e8e2da,#b9a596)"></div>
  <h3>Companionship</h3><p>Our goal is to keep your loved one active and engaged mentally and physically every day.</p><div class="plus">+</div>
</div>
<div class="card" style="left:355px">
  <div class="pic" role="img" aria-label="Caretaker helping a senior woman dress" style="background:linear-gradient(135deg,#8fc3d8,#c9a48c)"></div>
  <h3>Personal Care</h3><p>Our caretakers can offer a helping hand for dressing, bathing, or using the bathroom safely.</p><div class="plus">+</div>
</div>
<div class="card" style="left:612px">
  <div class="pic" role="img" aria-label="Caregiver tidying a kitchen" style="background:linear-gradient(135deg,#c2574a,#d8cfc5)"></div>
  <h3>Housekeeping</h3><p>Having a clean living space is essential for maintaining optimal health.</p><div class="plus">+</div>
</div>
<div class="card" style="left:870px">
  <div class="pic" role="img" aria-label="Caregiver helping a senior into a vehicle" style="background:linear-gradient(135deg,#4d5a6a,#9a7f88)"></div>
  <h3>Transportation</h3><p>Let us take the wheel, driving your loved one to appointments, running errands and more.</p><div class="plus">+</div>
</div>

<!-- Why choose us -->
<section class="abs why"></section>
<h2 class="abs section-title" style="left:0;width:1200px;text-align:center;top:1575px">Why <span>Choose Us</span></h2>
<div class="divider" style="left:405px;top:1623px;width:390px"><i></i><svg width="24" height="20" viewBox="0 0 24 20"><path d="M3 10L12 2l9 8M6 8v10h12V8" fill="none" stroke="#777" stroke-width="1.5"/></svg><i></i></div>
<p class="abs why-text">Serving the Inland Empire including Chino, Chino Hills, Corona, Eastvale, Jurupa Valley, Norco, Moreno Valley, Ontario, Rancho Cucamonga, Riverside, Redlands, San Bernardino and all other inland communities.</p>
<ul class="checks" style="left:100px">
  <li><svg width="16" height="16" viewBox="0 0 16 16"><rect x="1" y="1" width="14" height="14" fill="#fff" stroke="#555"/><path d="M4 8l3 3 6-8" fill="none" stroke="#333" stroke-width="2"/></svg>Family Owned</li>
  <li><svg width="16" height="16" viewBox="0 0 16 16"><rect x="1" y="1" width="14" height="14" fill="#fff" stroke="#555"/><path d="M4 8l3 3 6-8" fill="none" stroke="#333" stroke-width="2"/></svg>Insured</li>
  <li><svg width="16" height="16" viewBox="0 0 16 16"><rect x="1" y="1" width="14" height="14" fill="#fff" stroke="#555"/><path d="M4 8l3 3 6-8" fill="none" stroke="#333" stroke-width="2"/></svg>All employees pre-screened</li>
  <li><svg width="16" height="16" viewBox="0 0 16 16"><rect x="1" y="1" width="14" height="14" fill="#fff" stroke="#555"/><path d="M4 8l3 3 6-8" fill="none" stroke="#333" stroke-width="2"/></svg>Detailed written care plan</li>
  <li><svg width="16" height="16" viewBox="0 0 16 16"><rect x="1" y="1" width="14" height="14" fill="#fff" stroke="#555"/><path d="M4 8l3 3 6-8" fill="none" stroke="#333" stroke-width="2"/></svg>Licensed/Bonded</li>
</ul>
<ul class="checks" style="left:372px">
  <li><svg width="16" height="16" viewBox="0 0 16 16"><rect x="1" y="1" width="14" height="14" fill="#fff" stroke="#555"/><path d="M4 8l3 3 6-8" fill="none" stroke="#333" stroke-width="2"/></svg>Agency, not Registry</li>
  <li><svg width="16" height="16" viewBox="0 0 16 16"><rect x="1" y="1" width="14" height="14" fill="#fff" stroke="#555"/><path d="M4 8l3 3 6-8" fill="none" stroke="#333" stroke-width="2"/></svg>Worker's comp insurance included</li>
  <li><svg width="16" height="16" viewBox="0 0 16 16"><rect x="1" y="1" width="14" height="14" fill="#fff" stroke="#555"/><path d="M4 8l3 3 6-8" fill="none" stroke="#333" stroke-width="2"/></svg>We listen to your needs and requirements</li>
  <li><svg width="16" height="16" viewBox="0 0 16 16"><rect x="1" y="1" width="14" height="14" fill="#fff" stroke="#555"/><path d="M4 8l3 3 6-8" fill="none" stroke="#333" stroke-width="2"/></svg>Emphasis on mental and physical activity, engagement</li>
</ul>
<div class="abs why-photo" role="img" aria-label="Two caregivers laughing with a senior man at home"></div>

<!-- News -->
<h2 class="abs section-title" style="left:100px;top:1970px">Latest <span>News</span></h2>
<div class="abs pager"><b>‹</b><b class="next">›</b></div>
<div class="divider" style="left:100px;top:2022px;width:450px"><svg width="24" height="20" viewBox="0 0 24 20"><path d="M3 10L12 2l9 8M6 8v10h12V8" fill="none" stroke="#777" stroke-width="1.5"/></svg><i></i></div>
<article class="news-item" style="top:2065px"><div class="date"><div class="m">July</div><div class="d">08</div></div><h4>Sed ut perspiciatis unde omnis iste natus error sit voluptatem</h4><p>Accusant doloremque laudantium, totamrem aperiam, moregi eaquemn ipsa quae ab illoi facilies.</p></article>
<article class="news-item" style="top:2150px"><div class="date"><div class="m">July</div><div class="d">08</div></div><h4>Sed ut perspiciatis unde omnis iste natus error sit voluptatem</h4><p>Accusant doloremque laudantium, totamrem aperiam, moregi eaquemn ipsa quae ab illoi facilies.</p></article>
<article class="news-item" style="top:2235px"><div class="date"><div class="m">July</div><div class="d">08</div></div><h4>Sed ut perspiciatis unde omnis iste natus error sit voluptatem</h4><p>Accusant doloremque laudantium, totamrem aperiam, moregi eaquemn ipsa quae ab illoi facilies.</p></article>

<!-- FAQ -->
<h2 class="abs section-title" style="left:635px;top:1970px">FAQ<span>'s</span></h2>
<div class="divider" style="left:635px;top:2022px;width:465px"><svg width="24" height="20" viewBox="0 0 24 20"><path d="M3 10L12 2l9 8M6 8v10h12V8" fill="none" stroke="#777" stroke-width="1.5"/></svg><i></i></div>
<div class="faq" style="top:2067px">1. Are you licensed and insured?<span class="toggle">+</span></div>
<div class="faq" style="top:2112px">2. Are there any hidden fees?<span class="toggle">+</span></div>
<div class="faq" style="top:2157px">3. Are your employees fully vetted?<span class="toggle">+</span></div>
<div class="faq open" style="top:2202px">4. What if my caregiver cancels?<span class="toggle">–</span></div>
<p class="abs faq-body">On the rare occasion that your caregiver cannot make their appointment, we will send another carefully screened employee in their place.</p>

<!-- Reviews -->
<section class="abs reviews"></section>
<h2 class="abs section-title" style="left:0;width:1200px;text-align:center;top:2378px">Client <span>Reviews</span></h2>
<div class="divider" style="left:405px;top:2427px;width:390px"><i></i><svg width="24" height="20" viewBox="0 0 24 20"><path d="M3 10L12 2l9 8M6 8v10h12V8" fill="none" stroke="#777" stroke-width="1.5"/></svg><i></i></div>
<svg class="abs" style="left:305px;top:2512px" width="14" height="30" viewBox="0 0 14 30"><path d="M12 2L2 15l10 13" fill="none" stroke="#bbb" stroke-width="2"/></svg>
<svg class="abs" style="left:873px;top:2512px" width="14" height="30" viewBox="0 0 14 30"><path d="M2 2l10 13L2 28" fill="none" stroke="#bbb" stroke-width="2"/></svg>
<div class="avatar active" style="left:375px;background:#b9a394" role="img" aria-label="Client portrait"></div>
<div class="avatar" style="left:497px;background:#c9a07e" role="img" aria-label="Client portrait"></div>
<div class="avatar" style="left:618px;background:#cfc8c2" role="img" aria-label="Client portrait"></div>
<div class="avatar" style="left:739px;background:#b89a88" role="img" aria-label="Client portrait"></div>
<p class="abs quote"><span class="qmark">“</span>Sed ut perspiciatis unde omnis iste natus error sit voluptatem accusantium doloremque laudantium, totam rem aperiam, eaque ipsa quae ab illo inventore veritatis et quasi architecto beatae vitae dicta sunt explicabo. Nemo enim ipsam voluptatem quia voluptas sit aspernatur aut odit aut fugit, sed quia consequuntur magni dolores eos qui ratione voluptatem sequi nesciunt. Neque porro quisquam est, qui dolorem ipsum quia dolor sit amet<span class="qmark">”</span></p>

<!-- Footer -->
<footer class="abs footer"></footer>
<h5 class="footer-title" style="left:100px;width:150px">Quick Links</h5>
<ul class="quick-links">
  <li>Home</li><li>About Us</li><li>Services</li><li>Free In-Home Consultation</li><li>News</li><li>FAQ</li><li>Client Portal</li><li>Contact Us</li>
</ul>
<h5 class="footer-title" style="left:313px;width:230px">Contact Detail</h5>
<div class="contact" style="top:2812px">
  <svg width="14" height="18" viewBox="0 0 14 18"><path d="M7 0a7 7 0 0 0-7 7c0 5 7 11 7 11s7-6 7-11a7 7 0 0 0-7-7zm0 9.5A2.5 2.5 0 1 1 7 4.5a2.5 2.5 0 0 1 0 5z" fill="#ddd"/></svg>
  <div style="line-height:21px"><b style="font-weight:700">Willowmere Home Care</b><br>48 Linden Grove Lane,<br>Maple Court</div>
</div>
<div class="contact" style="top:2893px">
  <svg width="16" height="16" viewBox="0 0 24 24"><path fill="#ddd" d="M6.6 10.8a15 15 0 0 0 6.6 6.6l2.2-2.2c.3-.3.7-.4 1-.2 1.1.4 2.3.6 3.6.6.6 0 1 .4 1 1V20c0 .6-.4 1-1 1A17 17 0 0 1 3 4c0-.6.4-1 1-1h3.5c.6 0 1 .4 1 1 0 1.3.2 2.5.6 3.6.1.3 0 .7-.2 1z"/></svg>555 014 2290
</div>
<div class="contact" style="top:2935px">
  <svg width="16" height="16" viewBox="0 0 16 16"><rect x="3" y="1" width="10" height="5" fill="#ddd"/><rect x="1" y="6" width="14" height="6" fill="#ddd"/><rect x="4" y="10" width="8" height="5" fill="#ddd" stroke="#2b2b2b"/></svg>555 014 2290
</div>
<div class="contact" style="top:2976px">
  <svg width="16" height="12" viewBox="0 0 16 12"><rect width="16" height="12" fill="#ddd"/><path d="M0 0l8 7 8-7" fill="none" stroke="#2b2b2b"/></svg>info@willowmerehomecare.com
</div>
<h5 class="footer-title" style="left:613px;width:272px">Quick Contact</h5>
<div class="field" style="top:2810px;height:32px">Name</div>
<div class="field" style="top:2852px;height:32px">Email</div>
<div class="field" style="top:2894px;height:54px">Message</div>
<div class="btn" style="left:613px;top:2956px;width:118px;height:34px;font-size:14px">Submit</div>
<div class="abs footer-brand">
  <div class="mark"></div>
  <div class="name">Willowmere<br>Home Care</div>
</div>
<div class="abs copyright">© 2016 Willowmere Home Care. All Rights Reserved.</div>

</body>
</html>
```